Vireo Kinetics LLC Sports Therapy and Soft Tissue Injury solutions

We are a company that specializes in Sports Therapy, Physical therapy, muscular rehab, nutrition plans, and personal training. Vireo Kinetics travels around the country and world treating athletes and people in the workforce that have Soft Tissue injuries. We are legally partnered with QMD(Fluent Motion Protocols/fluentmotion.example) in treating endurance athletes ex. SteelWave triathalon. We educate our patients on how to sustain a healthy lifestyle.We need a web design that has a Home page summarizing our services, a Physical therapy page, a Personal training and nutrition page. Our ultimate goal is to build relationships with fitness centers, training facilities, and companies that are implementing preventative health measures for their employees. We want to incorporate the QMD logo and Steelwave logo attached in the website but, we want to use our own name (Vireo Kinetics LLC) as the main draw. We will provide literature for the website.

Target Market(s)

Brisk rig training gyms, Fitness centers, Dance studios, Companies looking for Corporate Wellness programs

Industry/Entity Type

Health And Wellness

Number of Pages Required

4 page

Font styles to use
Sans Serif

Requirements
Must have
• Stock Photos of Athletes training. Examples of Endurance Athletes and Cross training. A mesh of as many sports and training methods as possible. We are a new company and don't have many photos. Easy accessibility to change and add text as the company grows. Fluent Motion protocols logo incorporated in the back ground of the website. Always visible but does not take over the web page
Nice to have
• Sleek and cool, and masculine design. We want the website to stand out without focusing on one individual. We want to use the website to brand the company (Vireo Kinetics LLC) with easy access to social media platforms

```html
<!DOCTYPE html>
<html lang="en">
<head>
<meta charset="utf-8">
<title>Vireo Kinetics LLC</title>
<link href="https://fonts.googleapis.com/css2?family=Raleway:wght@600;700;800&family=Roboto:ital,wght@0,400;0,500;0,700;1,400&display=swap" rel="stylesheet">
<style>
:root{
  --brand:#0f4fb0;
  --band:#0d50b2;
  --ink:#1a1a1a;
  --muted:#6f6f6f;
  --pale-blue:#eef4fb;
  --pale-grey:#f5f5f5;
  --white:#ffffff;
}
*{box-sizing:border-box;margin:0;padding:0}
html,body{width:1200px;height:2903px;overflow:hidden}
body{font-family:"Roboto",Arial,sans-serif;color:var(--ink);background:var(--white);position:relative}
.heading{font-family:"Raleway",Arial,sans-serif;font-weight:800;color:var(--ink)}

/* header */
.site-header{position:absolute;top:0;left:0;width:1200px;height:78px;border-top:3px solid var(--brand);background:var(--white)}
.brand{position:absolute;left:99px;top:20px;font-family:"Raleway",Arial,sans-serif;font-size:31px;font-weight:700;color:var(--brand);letter-spacing:.3px}
.main-nav{position:absolute;right:82px;top:30px;display:flex;gap:30px;font-size:14px;color:var(--ink)}

/* hero */
.hero{position:absolute;top:78px;left:0;width:1200px;height:483px;overflow:hidden}
.hero-photo{position:absolute;inset:0;background:linear-gradient(90deg,#1e2b1c 0%,#2f4326 35%,#56683a 62%,#34402a 80%,#4a5a38 100%)}
.hero-shade{position:absolute;inset:0;background:linear-gradient(90deg,rgba(0,0,0,.35),rgba(0,0,0,0) 60%)}
.hero-title{position:absolute;left:122px;top:120px;font-family:"Raleway",Arial,sans-serif;font-weight:800;font-size:60px;color:var(--white);letter-spacing:.5px}
.hero-text{position:absolute;left:124px;top:204px;width:520px;font-size:16px;line-height:27px;color:var(--white)}
.btn-ghost{position:absolute;left:124px;top:288px;width:162px;height:38px;border:2px solid var(--white);color:var(--white);font-size:14px;font-weight:500;display:flex;align-items:center;justify-content:center}
.hero-arrow{position:absolute;top:208px}

/* about */
.about-panel{position:absolute;top:561px;left:490px;width:710px;height:300px;background:var(--pale-blue)}
.about-photo{position:absolute;top:523px;left:99px;width:489px;height:284px;background:linear-gradient(135deg,#3b3f4a 0%,#7a6a5c 40%,#c9b9a8 70%,#eae6e2 100%)}
.play{position:absolute;left:298px;top:625px}
.about-caption{position:absolute;left:99px;top:818px;font-size:18px;font-weight:500;color:var(--brand)}
.about-sub{position:absolute;left:99px;top:843px;font-size:12px;color:var(--muted)}
.about-title{position:absolute;left:629px;top:605px;font-size:29px}
.about-text{position:absolute;left:629px;top:656px;width:475px;font-size:12.5px;line-height:25px;color:#555;text-align:justify}
.btn-outline{position:absolute;border:1px solid #9aa8bb;color:var(--brand);font-size:13px;font-weight:500;display:flex;align-items:center;justify-content:center;background:var(--white)}
.about-btn{left:629px;top:759px;width:102px;height:35px}

/* services */
.section-title{position:absolute;left:0;width:1200px;text-align:center;font-size:29px}
.service{position:absolute;top:1001px;width:240px;text-align:center}
.service-ring{width:204px;height:204px;margin:0 auto;border:2px solid var(--brand);border-radius:50%;padding:6px}
.service-photo{width:100%;height:100%;border-radius:50%}
.service-name{margin-top:20px;font-size:20px;font-weight:500}
.service-text{margin-top:8px;font-size:12px;line-height:21px;color:var(--muted);padding:0 16px}

/* testimonial */
.quote-band{position:absolute;top:1364px;left:0;width:1200px;height:319px;background:var(--band)}
.band-arrow{position:absolute;top:1504px}
.quote-mark{position:absolute;left:578px;top:1422px}
.quote-text{position:absolute;left:228px;top:1485px;width:744px;text-align:center;font-style:italic;font-size:12px;line-height:25px;color:var(--white)}
.quote-by{position:absolute;left:0;width:1200px;text-align:center;color:var(--white);font-weight:700;font-size:15px}

/* what we do */
.wwd-title{position:absolute;left:99px;top:1738px;font-size:31px}
.wwd-text{position:absolute;left:99px;top:1790px;width:440px;font-size:12.5px;line-height:25px;color:#444}
.checks{position:absolute;left:99px;top:1852px;width:470px;display:grid;grid-template-columns:250px 220px;row-gap:12px;font-size:12.5px;color:#333}
.checks li{list-style:none;display:flex;align-items:center;gap:14px;height:18px}
.wwd-btn{left:99px;top:1968px;width:102px;height:35px}

.ask-box{position:absolute;left:621px;top:1740px;width:445px;height:267px;background:var(--white);border:1px solid #e4e4e4;box-shadow:0 0 8px rgba(0,0,0,.06)}
.ask-title{position:absolute;left:0;top:26px;width:100%;text-align:center;font-size:22px;font-weight:500;color:var(--brand)}
.ask-sub{position:absolute;left:0;top:58px;width:100%;text-align:center;font-size:13px;color:#555}
.field{position:absolute;border:1px solid #dadada;background:#f6f6f6;font-size:10.5px;color:#9a9a9a;padding:10px 10px}
.submit{position:absolute;left:28px;top:200px;width:186px;height:35px;background:var(--brand);color:var(--white);font-size:13px;font-weight:700;display:flex;align-items:center;justify-content:center;border-radius:2px}

/* blog */
.blog{position:absolute;top:2065px;left:0;width:1200px;height:508px;background:var(--pale-grey)}
.blog-sub{position:absolute;left:0;top:2160px;width:1200px;text-align:center;font-size:12.5px;color:#555}
.post{position:absolute;top:2212px;width:311px}
.post-photo{height:166px}
.post-title{margin-top:27px;font-family:"Raleway",Arial,sans-serif;font-weight:700;font-size:17px}
.post-text{margin-top:12px;font-size:12px;line-height:23px;color:#444}

/* footer */
.footer{position:absolute;top:2573px;left:0;width:1200px;height:277px;border-top:3px solid var(--brand);background:var(--white)}
.foot-col{position:absolute;top:2626px}
.foot-title{font-family:"Raleway",Arial,sans-serif;font-weight:700;font-size:17px;letter-spacing:.4px;margin-bottom:18px}
.foot-list{list-style:none;font-size:12.5px;color:#444}
.foot-list li{height:30px}
.contact-list li{display:flex;gap:14px;align-items:flex-start;line-height:23px;height:auto;margin-bottom:8px}
.partner-shape{position:absolute;background:#d5d5d5}
.bottom-bar{position:absolute;top:2850px;left:0;width:1200px;height:53px;border-top:1px solid #e6e6e6;text-align:center;font-size:12.5px;line-height:53px;color:#333}
</style>
</head>
<body>

<header class="site-header">
  <div class="brand">VIREO KINETICS LLC</div>
  <nav class="main-nav"><span>Home</span><span>Services</span><span>Physical Therapy</span><span>Personal Training</span><span>Nutrition</span><span>Contact us</span></nav>
</header>

<section class="hero">
  <div class="hero-photo" role="img" aria-label="Photo of an athlete stretching outdoors on a forest trail"></div>
  <div class="hero-shade"></div>
  <h1 class="hero-title">VIREO KINETICS</h1>
  <p class="hero-text">Vireo Kinetics travels around the country and world treating athletes and people in the workforce that have Soft Tissue injuries.</p>
  <div class="btn-ghost">GET MORE INFO</div>
  <svg class="hero-arrow" style="left:24px" width="30" height="66" viewBox="0 0 30 66"><polyline points="28,2 2,33 28,64" fill="none" stroke="rgba(255,255,255,.6)" stroke-width="2"/></svg>
  <svg class="hero-arrow" style="right:24px" width="30" height="66" viewBox="0 0 30 66"><polyline points="2,2 28,33 2,64" fill="none" stroke="rgba(255,255,255,.6)" stroke-width="2"/></svg>
</section>

<section>
  <div class="about-panel"></div>
  <div class="about-photo" role="img" aria-label="Photo of a therapist treating an athlete's ankle"></div>
  <svg class="play" width="90" height="90" viewBox="0 0 90 90"><circle cx="45" cy="45" r="42" fill="rgba(20,20,20,.65)"/><polygon points="40,37 52,45 40,53" fill="#fff"/></svg>
  <div class="about-caption">Vireo Kinetics Travels</div>
  <div class="about-sub">around the country and world treating athletes</div>
  <h2 class="heading about-title">ABOUT VIREO KINETICS</h2>
  <p class="about-text">It is a long established fact that a reader will be distracted by the readable content of a page when looking at its layout. The point of using Lorem Ipsum is that it has a more-or-less normal distribution of letters, as opposed</p>
  <div class="btn-outline about-btn">READ MORE</div>
</section>

<section>
  <h2 class="heading section-title" style="top:924px">OUR SERVICES</h2>
  <div class="service" style="left:83px">
    <div class="service-ring"><div class="service-photo" role="img" aria-label="Photo of sports massage on a shoulder" style="background:radial-gradient(circle at 40% 45%,#b07a5c,#5a3a2c 60%,#2a2220)"></div></div>
    <div class="service-name">Sports Therapy</div>
    <p class="service-text">Contrary to popular belief, Lorem Ipsum is not simply random text.</p>
  </div>
  <div class="service" style="left:346px">
    <div class="service-ring"><div class="service-photo" role="img" aria-label="Photo of a physical therapy session" style="background:radial-gradient(circle at 50% 40%,#c9b49a,#7c6a58 60%,#3a3430)"></div></div>
    <div class="service-name">Physical Therapy</div>
    <p class="service-text">Contrary to popular belief, Lorem Ipsum is not simply random text.</p>
  </div>
  <div class="service" style="left:608px">
    <div class="service-ring"><div class="service-photo" role="img" aria-label="Photo of knee rehabilitation treatment" style="background:radial-gradient(circle at 50% 50%,#f3e9e2,#cfdde6 55%,#7fb0cc)"></div></div>
    <div class="service-name">Muscular Rehab</div>
    <p class="service-text">Contrary to popular belief, Lorem Ipsum is not simply random text.</p>
  </div>
  <div class="service" style="left:869px">
    <div class="service-ring"><div class="service-photo" role="img" aria-label="Photo of fresh vegetables, eggs and nuts" style="background:radial-gradient(circle at 45% 45%,#d8442c,#9a2a1c 45%,#4a6a2a 80%,#2e3a1a)"></div></div>
    <div class="service-name">Nutrition Plans</div>
    <p class="service-text">Contrary to popular belief, Lorem Ipsum is not simply random text.</p>
  </div>
</section>

<section class="quote-band" role="img" aria-label="Blue band with a faint geometric pattern"></section>
<svg class="band-arrow" style="left:18px" width="14" height="40" viewBox="0 0 14 40"><polyline points="12,2 2,20 12,38" fill="none" stroke="rgba(255,255,255,.35)" stroke-width="2"/></svg>
<svg class="band-arrow" style="right:18px" width="14" height="40" viewBox="0 0 14 40"><polyline points="2,2 12,20 2,38" fill="none" stroke="rgba(255,255,255,.35)" stroke-width="2"/></svg>
<svg class="quote-mark" width="44" height="44" viewBox="0 0 44 44"><circle cx="22" cy="22" r="20" fill="none" stroke="#fff" stroke-width="2"/><text x="22" y="31" text-anchor="middle" font-family="Georgia,serif" font-size="24" font-weight="700" fill="#fff">&#8220;</text></svg>
<p class="quote-text">There are many variations of passages of Lorem Ipsum available, but the majority have suffered alteration in some form, by injected humour, or randomised words which don't look even slightly believable. If you are going to use a passage There are many variations of passages of Lorem Ipsum available, but the majority have suffered alteration in some form, by injected humour</p>
<div class="quote-by" style="top:1578px">By</div>
<div class="quote-by" style="top:1604px">Marek Tollan (Manager)</div>

<section>
  <h2 class="heading wwd-title">WHAT WE DO</h2>
  <p class="wwd-text">It is a long established fact that a reader will be distracted by the readable content of a page when looking at its layout.</p>
  <ul class="checks">
    <li><svg width="12" height="10" viewBox="0 0 12 10"><polyline points="1,5 4.5,8.5 11,1.5" fill="none" stroke="#0f4fb0" stroke-width="2"/></svg>Finibus Bonorum et Malorum</li>
    <li><svg width="12" height="10" viewBox="0 0 12 10"><polyline points="1,5 4.5,8.5 11,1.5" fill="none" stroke="#0f4fb0" stroke-width="2"/></svg>Finibus Bonorum et Malorum</li>
    <li><svg width="12" height="10" viewBox="0 0 12 10"><polyline points="1,5 4.5,8.5 11,1.5" fill="none" stroke="#0f4fb0" stroke-width="2"/></svg>Finibus Bonorum Malorum</li>
    <li><svg width="12" height="10" viewBox="0 0 12 10"><polyline points="1,5 4.5,8.5 11,1.5" fill="none" stroke="#0f4fb0" stroke-width="2"/></svg>Finibus Bonorum Malorum</li>
    <li><svg width="12" height="10" viewBox="0 0 12 10"><polyline points="1,5 4.5,8.5 11,1.5" fill="none" stroke="#0f4fb0" stroke-width="2"/></svg>Finibus Bonorum et Malorum</li>
    <li><svg width="12" height="10" viewBox="0 0 12 10"><polyline points="1,5 4.5,8.5 11,1.5" fill="none" stroke="#0f4fb0" stroke-width="2"/></svg>Finibus Bonorum et Malorum</li>
  </ul>
  <div class="btn-outline wwd-btn">READ MORE</div>

  <div class="ask-box">
    <div class="ask-title">ASK A QUESTION</div>
    <div class="ask-sub">Our team of highly trained professionals</div>
    <div class="field" style="left:28px;top:96px;width:186px;height:35px">Name</div>
    <div class="field" style="left:230px;top:96px;width:186px;height:35px">Mail id</div>
    <div class="field" style="left:28px;top:148px;width:186px;height:35px">Phone number</div>
    <div class="field" style="left:230px;top:148px;width:186px;height:87px">Type your questions ...</div>
    <div class="submit">SUBMIT NOW</div>
  </div>
</section>

<section class="blog"></section>
<h2 class="heading section-title" style="top:2118px">OUR RECENT BLOG POST</h2>
<p class="blog-sub">There are variations of passages Lorem Ipsum</p>
<article class="post" style="left:99px">
  <div class="post-photo" role="img" aria-label="Photo of an athlete wrapping hand wraps" style="background:linear-gradient(135deg,#1a1a1a,#3a2a2e 50%,#c84a7a 75%,#1c1c1c)"></div>
  <h3 class="post-title">SED PERSPICIATIS UNDE OMNIS</h3>
  <p class="post-text">Lorem ipsum dolor sit amet, consectetuer. Proin gravida nibh vel velit auctor aliquet. the far Aenean sollicitudi ravida.Lorem ipsum dolor sit amet,</p>
</article>
<article class="post" style="left:445px">
  <div class="post-photo" role="img" aria-label="Photo of people running on treadmills in a gym" style="background:linear-gradient(135deg,#2a3a5a,#6a86b0 45%,#c8d4e4 70%,#3a4a6a)"></div>
  <h3 class="post-title">SED PERSPICIATIS UNDE OMNIS</h3>
  <p class="post-text">Lorem ipsum dolor sit amet, consectetuer. Proin gravida nibh vel velit auctor aliquet. the far Aenean sollicitudi ravida.Lorem ipsum dolor sit amet,</p>
</article>
<article class="post" style="left:791px">
  <div class="post-photo" role="img" aria-label="Photo of an athlete training with suspension straps" style="background:linear-gradient(135deg,#1e1a18,#4a3a30 45%,#8a6a52 65%,#221c1a)"></div>
  <h3 class="post-title">SED PERSPICIATIS UNDE OMNIS</h3>
  <p class="post-text">Lorem ipsum dolor sit amet, consectetuer. Proin gravida nibh vel velit auctor aliquet. the far Aenean sollicitudi ravida.Lorem ipsum dolor sit amet,</p>
</article>

<footer class="footer"></footer>
<div class="foot-col" style="left:99px;width:200px">
  <div class="foot-title">CONTACT US</div>
  <ul class="foot-list contact-list">
    <li><svg width="10" height="14" viewBox="0 0 10 14" style="margin-top:4px;flex:none"><path d="M5 0a5 5 0 0 1 5 5c0 4-5 9-5 9S0 9 0 5a5 5 0 0 1 5-5z" fill="#0f4fb0"/><circle cx="5" cy="5" r="2" fill="#fff"/></svg><span>2000 years old. Alden Purcey, a Latin professor at</span></li>
    <li><svg width="12" height="12" viewBox="0 0 12 12" style="margin-top:5px;flex:none"><path d="M2 0l3 3-1.5 2a7 7 0 0 0 3.5 3.5L9 7l3 3-2 2C5 12 0 7 0 2z" fill="#0f4fb0"/></svg><span>Phone - 0400 555 018</span></li>
    <li><svg width="13" height="12" viewBox="0 0 13 12" style="margin-top:5px;flex:none"><rect x="0" y="3" width="13" height="9" fill="#0f4fb0"/><rect x="3" y="0" width="7" height="4" fill="#0f4fb0"/><rect x="3" y="6" width="7" height="3" fill="#fff"/></svg><span>Fax - 020 555 0147</span></li>
    <li style="white-space:nowrap"><svg width="13" height="10" viewBox="0 0 13 10" style="margin-top:6px;flex:none"><rect width="13" height="10" fill="#0f4fb0"/><polyline points="0,0 6.5,5.5 13,0" fill="none" stroke="#fff" stroke-width="1.2"/></svg><span>E-mail - info@vireokinetics.example</span></li>
  </ul>
</div>
<div class="foot-col" style="left:368px">
  <div class="foot-title">QUICK LINKS</div>
  <ul class="foot-list"><li>Home</li><li>About Us</li><li>Services</li><li>Blog</li></ul>
</div>
<div class="foot-col" style="left:559px">
  <div class="foot-title">SERVICES</div>
  <ul class="foot-list"><li>Sports Therapy</li><li>Physical therapy</li><li>Muscular rehab</li><li>Nutrition plans</li><li>Personal training.</li></ul>
</div>
<div class="foot-col" style="left:728px">
  <div class="foot-title">COMMUNITY</div>
  <ul class="foot-list"><li>Guidlines</li><li>Terms &amp; conditions</li><li>privacy policy</li><li>site map</li></ul>
</div>
<div class="partner-shape" role="img" aria-label="Partner badge" style="left:896px;top:2636px;width:206px;height:62px;border-radius:31px"></div>
<div class="partner-shape" role="img" aria-label="Partner badge" style="left:900px;top:2722px;width:196px;height:46px"></div>

<div class="bottom-bar">Copyrights@2017Compny name . All rights Reserved</div>

</body>
</html>
```